Event Planning Website

We are interested in redesigning our website. We just launched this company and we offer variety of event planning services. We specialize in wedding planning. We offer all inclusive packages, capturing the proposal, wedding planning, day of directing of the event. We help people save money, stay within budget and do the work so they could enjoy their special occasion.

We are looking to design 5 pages (we are open to suggestions to add or remove/combine), we like social media links (Facebook, instagram, yelp, testimonials) incorporated as recommended: Our existing webpage www.planwithpetal.com, Facebook.com/planwithpetal, http://instagram.com/planwithpetal, http://www.yelp.com/biz/plan-with-petal-san-ramon, logo and flyer are attached. Please let us know if you need additional information. We are looking for a template to be able to easily edit, fill and embed content.

HOME PAGE
This is the landing page, we want it to be informative, attractive, effective leading to contact/lead.

SERVICES
This page should be about our services which we offer (proposal, planning, day of directing), all packages with clean layout detailing the packages.

MEDIA
This page will consist of photo gallery of past events, social media feed, video clips etc.

CONTACT
Modern, hip, minimalistic.

About us
Who we are, the team, bio about each planner within our firm, experience,

Industry/Entity Type

Event Planning

```html
<!DOCTYPE html>
<html lang="en">
<head>
<meta charset="utf-8">
<title>Plan With Petal — Planning &amp; Coordination</title>
<link rel="stylesheet" href="https://fonts.googleapis.com/css2?family=Crimson+Text:wght@400;600;700&family=Libre+Baskerville:wght@400;700&family=Great+Vibes&display=swap">
<style>
:root{
  --pink:#dd55bd;
  --pink-dark:#c8429f;
  --orange:#f7b15e;
  --orange-soft:#f9c58a;
  --ink:#3a3a3a;
  --muted:#8b8b8b;
  --line:#cfcfcf;
  --page:#efefef;
  --white:#ffffff;
}
*{box-sizing:border-box;margin:0;padding:0}
html,body{width:819px;height:1200px;overflow:hidden}
body{position:relative;background:var(--page);font-family:"Crimson Text",Georgia,serif;color:var(--ink)}
.abs{position:absolute}
.site-header{left:0;top:0;width:819px;height:115px;background:var(--white);border-bottom:1px solid var(--line)}
.brand{left:72px;top:34px;display:flex;align-items:center;gap:8px}
.brand-mark{width:22px;height:22px;border-radius:50%;background:var(--ink)}
.brand-name{font-size:29px;letter-spacing:1px;color:var(--ink);line-height:1}
.brand-sub{left:114px;top:68px;font-size:8px;letter-spacing:1px;color:var(--ink)}
.social{left:611px;top:37px;display:flex;gap:7px}
.social span{width:21px;height:21px;border-radius:4px;display:block}
.social span:nth-child(odd){background:var(--pink)}
.social span:nth-child(even){background:var(--orange-soft)}
.phone{left:646px;top:59px;font-size:18px;color:var(--orange-soft);letter-spacing:.3px}
.main-nav{left:0;top:116px;width:819px;height:57px;background:var(--white);border-bottom:1px solid var(--line)}
.main-nav ul{list-style:none;display:flex;position:absolute;left:72px;top:14px}
.main-nav li{font-size:21px;color:#555;padding:0 18px;border-left:1px solid var(--line);line-height:24px}
.main-nav li:first-child{padding-left:0;border-left:none}
.search{left:612px;top:132px;width:135px;height:22px;border-radius:11px;background:#efefef;display:flex;align-items:center;padding-left:8px;font-size:10px;color:#888;gap:6px}
.search svg{flex:none}
.slider{left:72px;top:200px;width:675px;height:276px;background:var(--white);box-shadow:0 6px 14px rgba(0,0,0,.18)}
.slide-photo{left:82px;top:212px;width:655px;height:255px;background:linear-gradient(120deg,#556b3a 0%,#8b7a5a 40%,#d9b79a 55%,#6f7e4c 80%,#43552c 100%)}
.slide-caption{left:514px;top:392px;width:223px;height:61px;background:rgba(247,177,94,.88);color:var(--white);font-family:"Libre Baskerville",Georgia,serif;font-weight:700;font-size:14px;line-height:18px;padding:11px 0 0 11px;white-space:nowrap;overflow:hidden}
.arrow{top:317px;width:26px;height:45px}
.arrow.prev{left:46px}
.arrow.next{left:747px}
.content{left:71px;top:508px;width:676px;height:644px;background:var(--white);box-shadow:0 0 3px rgba(0,0,0,.08)}
.feature{top:519px;width:212px;height:140px;background:var(--white);border:1px solid #d6d6d6;padding:5px}
.feature-photo{width:100%;height:100%;position:relative;overflow:hidden}
.feature-label{position:absolute;left:14px;right:14px;bottom:10px;height:30px;background:rgba(240,166,80,.9);font-family:"Great Vibes",cursive;color:var(--white);font-size:19px;text-align:center;line-height:30px}
.f1{left:82px}.f1 .feature-photo{background:linear-gradient(135deg,#e6ecef,#b9c4c9 60%,#2d2d2d)}
.f2{left:304px}.f2 .feature-photo{background:linear-gradient(90deg,#5b4a3d,#c96b7f 40%,#f0e8e3 60%,#8a9a72)}
.f3{left:527px}.f3 .feature-photo{background:linear-gradient(180deg,#b34424,#7f2d16 55%,#e0d0c0)}
.promo{left:81px;top:693px;width:656px;height:48px;background:var(--pink)}
.promo-title{left:92px;top:693px;font-family:"Great Vibes",cursive;font-size:33px;color:var(--white);line-height:48px}
.btn-learn{left:642px;top:701px;width:90px;height:33px;border-radius:6px;background:var(--white);border:2px solid #f3c2e6;color:var(--pink);font-size:16px;text-align:center;line-height:29px}
.section-title{font-family:"Libre Baskerville",Georgia,serif;font-weight:700;font-size:18px;color:var(--orange-soft)}
.about-title{left:82px;top:769px}
.about-text{left:84px;top:803px;width:385px;font-size:13.5px;line-height:15.6px;color:#333}
.about-text p+p{margin-top:14px}
.btn-read{left:82px;top:947px;width:88px;height:31px;border-radius:5px;background:var(--orange-soft);color:var(--white);font-size:14px;display:flex;align-items:center;justify-content:center;gap:5px}
.testi-title{left:492px;top:770px}
.testimonial{left:492px;width:240px;display:flex;gap:12px}
.t1{top:803px}.t2{top:892px}
.avatar{width:68px;height:68px;border-radius:50%;border:4px solid var(--white);box-shadow:0 2px 5px rgba(0,0,0,.3);flex:none}
.t1 .avatar{background:radial-gradient(circle,#f1e6de,#b8a89b)}
.t2 .avatar{background:radial-gradient(circle,#f4efea,#7d6a5c)}
.testimonial h4{font-family:"Libre Baskerville",Georgia,serif;font-size:11px;line-height:13px;color:var(--ink);margin-top:5px}
.testimonial p{font-size:9px;line-height:10.5px;color:#444;margin-top:4px}
.divider{left:492px;top:882px;width:239px;height:1px;background:var(--line)}
.footer-copy{left:72px;top:1158px;font-size:9px;color:var(--muted)}
.footer-links{left:586px;top:1157px;font-size:9px;color:var(--muted);display:flex;gap:8px}
.footer-badge{left:299px;top:1120px;width:210px;height:140px;border-radius:50%;background:#eeeeee;border:1px solid #dcdcdc;display:flex;justify-content:center;padding-top:24px}
.footer-badge span{font-size:21px;color:#a9a9a9;letter-spacing:1px}
</style>
</head>
<body>
<header class="site-header abs">
  <div class="brand abs"><span class="brand-mark"></span><span class="brand-name">PLAN WITH PETAL</span></div>
  <div class="brand-sub abs">PLANNING &amp; COORDINATION</div>
  <div class="social abs" aria-label="Social links"><span></span><span></span><span></span><span></span><span></span></div>
  <div class="phone abs">(888) 555-0142</div>
</header>

<nav class="main-nav abs">
  <ul><li>Home</li><li>Services</li><li>Media</li><li>Contact</li><li>About</li></ul>
</nav>
<div class="search abs">
  <svg width="12" height="12" viewBox="0 0 12 12"><circle cx="5" cy="5" r="3.6" fill="none" stroke="#f7b15e" stroke-width="1.6"/><line x1="7.7" y1="7.7" x2="11" y2="11" stroke="#f7b15e" stroke-width="1.6"/></svg>
  Search..
</div>

<div class="slider abs"></div>
<div class="slide-photo abs" role="img" aria-label="Smiling bride in a garden with flowers in her hair"></div>
<div class="slide-caption abs">We help people Save Money,<br>Stay within Budget.</div>
<svg class="arrow prev abs" viewBox="0 0 26 45"><polygon points="26,0 26,45 10,45 0,22 10,0" fill="#dd55bd"/><polyline points="17,14 10,22.5 17,31" fill="none" stroke="#fff" stroke-width="3"/></svg>
<svg class="arrow next abs" viewBox="0 0 26 45"><polygon points="0,0 16,0 26,22 16,45 0,45" fill="#dd55bd"/><polyline points="9,14 16,22.5 9,31" fill="none" stroke="#fff" stroke-width="3"/></svg>

<main class="content abs"></main>

<div class="feature f1 abs"><div class="feature-photo" role="img" aria-label="Wedding rings on a planner notebook"><div class="feature-label">Wedding Planning</div></div></div>
<div class="feature f2 abs"><div class="feature-photo" role="img" aria-label="Couple holding a bouquet of roses"><div class="feature-label">Capturing the proposal</div></div></div>
<div class="feature f3 abs"><div class="feature-photo" role="img" aria-label="Decorated banquet hall with red table settings"><div class="feature-label">Inclusive packages</div></div></div>

<div class="promo abs"></div>
<div class="promo-title abs">Lorest Mesto Dinh Fennel Ellpitis</div>
<div class="btn-learn abs">Learn More</div>

<h2 class="section-title about-title abs">Lorest Mesto Dinh Fennel Ellpitis</h2>
<div class="about-text abs">
  <p>Nulla porta faucibus ante, sed faucibus justo malesuada eget.fhgh Integer cursus quam at arcu lacinia, ut auctor dui fringilla. Duisf aliquam facilisis massa sed pretium. Donec condimentum accum enim fringilla cursus. Nullam commodo vitae dolor in lobortis. ghrf Phasellus at varius leo. Integer eget suscipit risus.</p>
  <p>Pellentesque nec fringilla ante, a fermentum dolor.rgdf<br>Interdum et malesuada fames ac ante ipsum primis in faucibu</p>
</div>
<div class="btn-read abs">Read More <svg width="8" height="12" viewBox="0 0 8 12"><polyline points="1,1 6,6 1,11" fill="none" stroke="#fff" stroke-width="2.4"/></svg></div>

<h2 class="section-title testi-title abs">Testimonials</h2>
<div class="testimonial t1 abs">
  <div class="avatar" role="img" aria-label="Portrait of a bride"></div>
  <div><h4>Nulla porta faucibus ansfk sdfhlhodsfite</h4><p>Nulla porta faucibus antefgduifg dsfuhuhdsfg udefghu wufe lkdef eswdfgh .</p></div>
</div>
<div class="divider abs"></div>
<div class="testimonial t2 abs">
  <div class="avatar" role="img" aria-label="Portrait of a bride in a veil"></div>
  <div><h4>Nulla porta faucibus ansfk sdfhlhodsfite</h4><p>Nulla porta faucibus antefgduifg dsfuhuhdsfg udefghu wufe lkdef eswdfgh .</p></div>
</div>

<footer>
  <div class="footer-copy abs">© All Rights Reserved PWP</div>
  <div class="footer-badge abs"><span>PLAN WITH PETAL</span></div>
  <div class="footer-links abs"><span>Home</span><span>Service</span><span>Media</span><span>Contact</span><span>About</span></div>
</footer>
</body>
</html>
```